Restaurant Digital TV Menu Pictures

Need a digital menu board, image square of food. Something simple for customer to look and point to or say the food number. Image square 4x6, 5x7 or various of that. Vietnamese restaurant type food. I need template created and designer choice of design. Color scheme orange and white and little green. I would like to in the title of the food myself and written detail myself. I just need the template and possible have the design edit the picture a bit. Total food about 30 image will mostly be about 20-30 images. This will be display on a TV screen 16:9 size on a 55 inch tv. Attached is the food menu item. Also attach how the image off food will be taken. Also attach of other people design on the web. However, I would like number be label on the food item. I can find tune the correct information and food type and numbers later.

Font styles to use
Decorative

Colors
f37122
fffefb
9bcb3c

Requirements
Must have
• Photo edit food image basic making it pop. Make it look better, not magic, but better than my photography. Asian feel to the design.
Nice to have
• Fresh image of ingredients, (cilantro, freshly cook, non fast food) Image of green food

```html
<!DOCTYPE html>
<html lang="en">
<head>
<meta charset="utf-8">
<title>Menu Item 1</title>
<link rel="stylesheet" href="https://fonts.googleapis.com/css2?family=Poppins:wght@700&display=swap">
<style>
  :root {
    --orange: #f37122;
    --cream: #fffefb;
    --green: #6cbf45;
    --bowl: #2a2623;
    --sauce: #9a5a26;
  }
  html, body {
    margin: 0;
    padding: 0;
    width: 1199px;
    height: 1200px;
    overflow: hidden;
    background: var(--cream);
  }
  .menu-card {
    display: block;
    width: 1199px;
    height: 1200px;
  }
  .frame-line { fill: none; stroke: var(--green); }
  .frame-solid { stroke-width: 9; }
  .frame-dashed { stroke-width: 4; stroke-dasharray: 18 12; }
  .frame-thin { stroke-width: 3; }
  .accent-ring { fill: none; stroke: var(--orange); stroke-width: 8; }
  .accent-ring-small { fill: none; stroke: var(--green); stroke-width: 7; }
  .number-tile { fill: var(--orange); }
  .diagonal-bar { fill: var(--cream); stroke: var(--green); stroke-width: 6; }
  .item-number {
    font-family: "Poppins", sans-serif;
    font-weight: 700;
    font-size: 290px;
    fill: var(--cream);
  }
</style>
</head>
<body>
<svg class="menu-card" viewBox="0 0 1000 1000" preserveAspectRatio="none" xmlns="http://www.w3.org/2000/svg">
  <defs>
    <radialGradient id="dish-tones" cx="0.35" cy="0.45" r="0.75">
      <stop offset="0" stop-color="#c98a45"/>
      <stop offset="0.35" stop-color="#9a5a26"/>
      <stop offset="0.62" stop-color="#5b3a22"/>
      <stop offset="0.8" stop-color="#2a2623"/>
      <stop offset="1" stop-color="#e9e4dc"/>
    </radialGradient>
  </defs>

  <rect class="dish-photo" x="0" y="0" width="695" height="715" fill="url(#dish-tones)"
        role="img" aria-label="Photo of a rice bowl with glazed chicken, fried egg, fresh salad and a spring roll"/>

  <rect class="frame-line frame-solid" x="6" y="6" width="686" height="704"/>

  <path class="frame-line frame-dashed" d="M713 10 V560"/>
  <path class="frame-line frame-dashed" d="M30 740 H615"/>

  <path class="frame-line frame-thin" d="M975 75 V575 H845"/>
  <path class="frame-line frame-thin" d="M30 810 V975 H580"/>

  <circle class="accent-ring" cx="425" cy="440" r="335"/>

  <rect class="number-tile" x="612" y="625" width="388" height="375"/>
  <text class="item-number" x="803" y="922" text-anchor="middle">1</text>

  <circle class="accent-ring-small" cx="662" cy="648" r="80"/>

  <rect class="diagonal-bar" x="420" y="-11" width="480" height="22"
        transform="translate(662 660) rotate(-45) translate(-660 0)"/>
</svg>
</body>
</html>
```